Design a New Business Card for Our Company

We are looking for fresh, unique, and a modern business card that reflects our roots as digital marketing agency focused on SEM.

Industry/Entity Type

Marketing

Contact Information for Business Card

looking for very unique out of the box designs. clean and modern that compliments our logo

Requirements
Must have
• colors should match our logo
• Front should have name, address, email, and phone/fax of the person, phone/fax are the same number
• back should have our url

```html
<!DOCTYPE html>
<html lang="en">
<head>
<meta charset="utf-8">
<title>Tidewell Solutions – Business Card</title>
<link rel="stylesheet" href="https://fonts.googleapis.com/css2?family=Arimo:wght@400;700&display=swap">
<style>
  :root {
    --page-bg: #e9ecec;
    --card-white: #ffffff;
    --card-white-shade: #eef2f8;
    --brand-blue: #4f8fd3;
    --brand-blue-deep: #4677a6;
    --brand-blue-light: #5d95cf;
    --accent-cyan: #7ff2f6;
    --text-dark: #2f3338;
    --text-muted: #6d7176;
    --icon-blue: #6a9fd8;
    --white: #ffffff;
  }
  * { box-sizing: border-box; margin: 0; padding: 0; }
  html, body {
    width: 1200px; height: 1200px; overflow: hidden;
    background: var(--page-bg);
    font-family: "Arimo", Arial, sans-serif;
  }
  .sheet {
    width: 1200px; height: 1200px;
    display: flex; flex-direction: column; align-items: center; justify-content: center;
    gap: 52px;
  }
  .card {
    position: relative;
    width: 900px; height: 514px;
    box-shadow: 0 6px 18px rgba(0,0,0,0.12);
    overflow: hidden;
  }

  /* ---------- Front ---------- */
  .card-front {
    background: linear-gradient(160deg, var(--card-white) 55%, var(--card-white-shade) 100%);
  }
  .edge-bar {
    position: absolute; width: 12px; background: var(--brand-blue);
    border-radius: 2px;
  }
  .edge-bar-left { left: 0; top: 250px; height: 190px; }
  .edge-bar-right { right: 0; top: 40px; height: 120px; }

  .front-brand {
    position: absolute; left: 390px; top: 58px;
    display: flex; align-items: center; gap: 16px;
  }
  .brand-dot {
    width: 44px; height: 44px; border-radius: 50%;
    background: var(--brand-blue);
  }
  .brand-name {
    font-weight: 700; letter-spacing: -1px; line-height: 1;
  }
  .front-brand .brand-name { font-size: 66px; color: var(--brand-blue); }
  .brand-tagline {
    font-weight: 400; text-transform: uppercase; letter-spacing: 22px;
  }
  .front-brand .brand-tagline {
    font-size: 15px; color: var(--text-muted); margin-top: 6px;
  }

  .person {
    position: absolute; right: 48px; top: 176px; text-align: right;
  }
  .person-name {
    font-size: 34px; font-weight: 700; color: var(--brand-blue);
    letter-spacing: 0.5px;
  }
  .person-title {
    font-size: 20px; color: var(--text-dark); margin-top: 6px;
  }

  .contact-list {
    position: absolute; left: 68px; top: 270px;
    list-style: none; display: flex; flex-direction: column; gap: 16px;
  }
  .contact-item {
    display: flex; align-items: center; gap: 22px;
    font-size: 23px; color: var(--text-dark);
  }
  .contact-icon { width: 30px; height: 30px; flex: none; }

  /* ---------- Back ---------- */
  .card-back {
    background: linear-gradient(135deg, var(--brand-blue-light) 0%, var(--brand-blue-deep) 100%);
    display: flex; align-items: center; justify-content: center;
  }
  .back-brand { display: flex; align-items: center; gap: 24px; }
  .back-brand .brand-dot {
    width: 70px; height: 70px; background: var(--accent-cyan);
  }
  .back-brand .brand-name { font-size: 112px; color: var(--white); }
  .back-brand .brand-tagline {
    font-size: 24px; color: var(--white); margin-top: 10px; letter-spacing: 30px;
  }
  .back-url {
    font-size: 20px; color: var(--white); letter-spacing: 8px; margin-top: 12px;
  }
</style>
</head>
<body>
<main class="sheet">

  <section class="card card-front" aria-label="Business card front">
    <span class="edge-bar edge-bar-left"></span>
    <span class="edge-bar edge-bar-right"></span>

    <div class="front-brand">
      <span class="brand-dot"></span>
      <div>
        <div class="brand-name">Tidewell</div>
        <div class="brand-tagline">Solutions</div>
      </div>
    </div>

    <div class="person">
      <div class="person-name">JOHN DOE</div>
      <div class="person-title">Director</div>
    </div>

    <ul class="contact-list">
      <li class="contact-item">
        <svg class="contact-icon" viewBox="0 0 30 30" aria-hidden="true">
          <circle cx="15" cy="15" r="13" fill="none" stroke="var(--icon-blue)" stroke-width="2"/>
          <path d="M10 9 l3 0 l1 4 l-2 1 a8 8 0 0 0 4 4 l1 -2 l4 1 l0 3 a2 2 0 0 1 -2 1 a12 12 0 0 1 -10 -10 a2 2 0 0 1 1 -2z" fill="var(--icon-blue)"/>
        </svg>
        <span>1-234-567890</span>
      </li>
      <li class="contact-item">
        <svg class="contact-icon" viewBox="0 0 30 30" aria-hidden="true">
          <circle cx="15" cy="15" r="13" fill="none" stroke="var(--icon-blue)" stroke-width="2"/>
          <rect x="10" y="8" width="10" height="5" fill="none" stroke="var(--icon-blue)" stroke-width="1.6"/>
          <rect x="8" y="13" width="14" height="6" rx="1" fill="var(--icon-blue)"/>
          <rect x="10" y="17" width="10" height="5" fill="var(--white)" stroke="var(--icon-blue)" stroke-width="1.6"/>
        </svg>
        <span>1-234-567890</span>
      </li>
      <li class="contact-item">
        <svg class="contact-icon" viewBox="0 0 30 30" aria-hidden="true">
          <circle cx="15" cy="15" r="13" fill="none" stroke="var(--icon-blue)" stroke-width="2"/>
          <rect x="8" y="10" width="14" height="10" rx="1" fill="var(--icon-blue)"/>
          <path d="M8 10 l7 6 l7 -6" fill="none" stroke="var(--white)" stroke-width="1.4"/>
        </svg>
        <span>john@companyname.com</span>
      </li>
      <li class="contact-item">
        <svg class="contact-icon" viewBox="0 0 30 30" aria-hidden="true">
          <circle cx="15" cy="15" r="13" fill="none" stroke="var(--icon-blue)" stroke-width="2"/>
          <path d="M15 22 c-4 -5 -6 -7 -6 -10 a6 6 0 0 1 12 0 c0 3 -2 5 -6 10z" fill="var(--icon-blue)"/>
          <circle cx="15" cy="12" r="2.2" fill="var(--white)"/>
        </svg>
        <span>Dummy city, Dummy Country Land</span>
      </li>
    </ul>
  </section>

  <section class="card card-back" aria-label="Business card back">
    <div class="back-brand">
      <span class="brand-dot"></span>
      <div>
        <div class="brand-name">Tidewell</div>
        <div class="brand-tagline">Solutions</div>
        <div class="back-url">www.companyname.com</div>
      </div>
    </div>
  </section>

</main>
</body>
</html>
```